Business cards for a tribute and obituary website

Our website is called Quiet Orchard.

It is a special place online for people to remember their loved ones who have passed away, through obituaries and tributes. Friends and family can also convey their condolences on the deceased's memorial page. Celebrating the life of the deceased and remembering their legacy is very important to us – death should not be just about grieving.

We would like the card to look tasteful and modern. The design should ideally not have colours that are too bright. The logo and website URL, www.quietorchardpages.net should be visible on the front of the card, with our slogan "Celebrating a life passed" on the back.

The design should communicate our purpose – remembering loved ones who have passed – and also a lighter tone of celebrating life. It should not look like a funeral director's card!

Our logo has been attached. Looking forward to some beautiful designs! Get creative :)
Updates

Reason: Thank you all for your designs. The rest of my team and I have not reached a decision on which design to select and I am collecting feedback from them. I will provide feedback for any changes that need to be made soon. It would be great if we could see more original designs and in more colours! We will definitely select a design by this deadline.

Industry/Entity Type

Business

Contact Information for Business Card

Nadia Fenwick
Project Manager
471226809
nadiafenwick@quietorchardpages.net

Font styles to use
Serif
Sans Serif

Requirements
Must have
• Logo and website address (www.quietorchardpages.net) on the front.
Nice to have
• Hi designers! It would be nice to see alternative colours – feel free to try out colours that are tasteful and subtle. The colour of the business card does not have to be the same as the logo.
• We would also like to see the logo used in different ways, perhaps a glossy or embossed finish. The card should look stylish.

```html
<!DOCTYPE html>
<html lang="en">
<head>
<meta charset="utf-8">
<title>Quiet Orchard – Business Cards</title>
<link rel="stylesheet" href="https://fonts.googleapis.com/css2?family=Old+Standard+TT:wght@400;700&display=swap">
<style>
  :root {
    --bg: #e4e5e7;
    --card: #ffffff;
    --navy: #0d2a4a;
    --blue-name: #2b8fd4;
    --blue-deep: #0b66bf;
    --blue-sky: #12ade8;
    --blue-soft: #6ccaf0;
    --blue-pale: #cde9f7;
    --ink: #1d2f45;
  }
  * { margin: 0; padding: 0; box-sizing: border-box; }
  html, body { width: 1200px; height: 1000px; overflow: hidden; }
  body {
    background: var(--bg);
    font-family: "Old Standard TT", Georgia, serif;
    color: var(--ink);
  }
  .card {
    position: absolute;
    left: 290px;
    width: 620px;
    height: 354px;
    background: var(--card);
    box-shadow: 0 6px 18px rgba(0,0,0,0.18);
    overflow: hidden;
  }
  .card--front { top: 90px; }
  .card--back { top: 520px; }

  .card__glow {
    position: absolute;
    right: 0;
    top: 0;
    width: 340px;
    height: 300px;
    background: radial-gradient(ellipse at 100% 20%, var(--blue-sky) 0%, var(--blue-soft) 25%, var(--blue-pale) 55%, rgba(255,255,255,0) 78%);
    opacity: 0.75;
  }
  .card__wash {
    position: absolute;
    left: 0;
    top: 0;
    width: 100%;
    height: 200px;
    background: linear-gradient(180deg, var(--blue-soft) 0%, var(--blue-pale) 45%, rgba(255,255,255,0) 100%);
    opacity: 0.8;
  }

  .brand { position: absolute; display: flex; align-items: center; gap: 8px; }
  .brand__mark { width: 22px; height: 22px; background: var(--navy); }
  .brand__name {
    font-weight: 700; color: var(--navy); font-size: 17px; line-height: 0.95;
  }
  .card--front .brand { left: 26px; top: 24px; }

  .person { position: absolute; left: 40px; top: 168px; }
  .person__name { font-size: 30px; color: var(--blue-name); font-weight: 400; line-height: 1; }
  .person__role { font-size: 15px; color: var(--ink); margin-top: 4px; }

  .contact {
    position: absolute; right: 30px; bottom: 34px;
    text-align: right; font-size: 13px; line-height: 1.75; color: var(--ink);
    font-style: normal;
  }

  .card--back .brand {
    left: 50%; top: 170px; transform: translateX(-50%);
    flex-direction: column; gap: 6px; text-align: center;
  }
  .card--back .brand__mark { width: 30px; height: 30px; }
  .card--back .brand__name { font-size: 14px; }
  .tagline {
    position: absolute; left: 0; right: 0; top: 252px;
    text-align: center; font-size: 20px; color: var(--blue-name);
  }
</style>
</head>
<body>

<section class="card card--front" aria-label="Card front">
  <div class="card__glow" role="img" aria-label="Decorative blue light rays fanning from the top right corner"></div>

  <div class="brand">
    <span class="brand__mark"></span>
    <span class="brand__name">Quiet<br>Orchard</span>
  </div>

  <div class="person">
    <h1 class="person__name">Nadia Fenwick</h1>
    <p class="person__role">Project Manager</p>
  </div>

  <address class="contact">
    471226809<br>
    nadiafenwick@quietorchardpages.net<br>
    www.quietorchardpages.net
  </address>
</section>

<section class="card card--back" aria-label="Card back">
  <div class="card__wash" role="img" aria-label="Decorative blue gradient panels across the top of the card"></div>

  <div class="brand">
    <span class="brand__mark"></span>
    <span class="brand__name">Quiet<br>Orchard</span>
  </div>

  <p class="tagline">Celebrating a life passed</p>
</section>

</body>
</html>
```